Groovy little Insurance brokerage needs a new look

We have a new logo, but need to work out how to make it work for us!
We are a small insurance broking firm (three staff with different focus and styles), with lots of energy, experience and enthusiasm. A focus on both commercial and domestic market. We would like our cards to show a fresh look - while veering away from the 'run of the mill' insurance industry (often dull) approach.
Updates

Thanks to all for your concepts.

Had some great ideas come back, now just the process of picking which one is going to work best for us...
Will advise when we've had an opportunity to review.

Thanks!
From the team at
Kestrel Dunmore Insurance Brokers

Thanks SO much to all of your for your great designs.  Now just a process of sorting out the favorites.  If yours is eliminated, just want to say a collective thank you for your efforts!

Industry/Entity Type

Business

```html
<!DOCTYPE html>
<html lang="en">
<head>
<meta charset="utf-8">
<title>Kestrel Dunmore Insurance Brokers – Business Cards</title>
<link rel="stylesheet" href="https://fonts.googleapis.com/css2?family=Lato:wght@400;700;900&display=swap">
<style>
  :root {
    --teal: #1aa6bf;
    --sky: #a9d8e4;
    --ink: #231f20;
    --paper: #ffffff;
    --backdrop: #e6e7e8;
  }
  * { box-sizing: border-box; margin: 0; padding: 0; }
  html, body {
    width: 1200px;
    height: 1000px;
    overflow: hidden;
    background: var(--backdrop);
    font-family: "Lato", sans-serif;
  }
  .card {
    position: absolute;
    top: 330px;
    width: 530px;
    height: 330px;
    background: var(--paper);
    box-shadow: 0 6px 18px rgba(0,0,0,0.12);
    overflow: hidden;
  }
  .card--front { left: 45px; }
  .card--back { left: 625px; }

  .brand {
    display: flex;
    align-items: flex-end;
    gap: 14px;
  }
  .brand__square {
    background: var(--teal);
    flex: none;
  }
  .brand__name {
    font-weight: 900;
    color: var(--ink);
    line-height: 0.8;
    letter-spacing: -2px;
  }
  .brand__tagline {
    color: var(--teal);
    font-weight: 700;
    letter-spacing: 0.5px;
    text-transform: uppercase;
  }

  /* Front */
  .card--front .brand-block {
    position: absolute;
    left: 70px;
    top: 95px;
  }
  .card--front .brand__square { width: 92px; height: 92px; }
  .card--front .brand__name { font-size: 118px; }
  .card--front .brand__tagline {
    font-size: 15px;
    margin: 10px 0 0 106px;
  }

  /* Back */
  .card--back .brand-block {
    position: absolute;
    left: 26px;
    top: 30px;
  }
  .card--back .brand__square { width: 66px; height: 66px; }
  .card--back .brand__name { font-size: 84px; }
  .card--back .brand__tagline {
    font-size: 11px;
    margin: 8px 0 0 80px;
  }
  .contact {
    position: absolute;
    left: 106px;
    top: 158px;
  }
  .contact__name {
    color: var(--teal);
    font-size: 22px;
    font-weight: 400;
    letter-spacing: 0.5px;
    margin-bottom: 14px;
  }
  .contact__row {
    font-size: 15px;
    line-height: 1.65;
    color: var(--ink);
  }
  .contact__label { color: var(--teal); }
  .footer-band {
    position: absolute;
    left: 0;
    right: 0;
    bottom: 0;
    height: 14px;
    background: var(--sky);
  }
  .web-tab {
    position: absolute;
    right: 40px;
    bottom: 0;
    width: 260px;
    height: 40px;
    background: var(--teal);
    border-radius: 6px 6px 0 0;
    color: var(--paper);
    font-size: 16px;
    font-weight: 700;
    letter-spacing: 0.5px;
    display: flex;
    align-items: center;
    justify-content: center;
  }
</style>
</head>
<body>

<section class="card card--front" aria-label="Card front">
  <div class="brand-block">
    <div class="brand">
      <span class="brand__square"></span>
      <span class="brand__name">kdib</span>
    </div>
    <p class="brand__tagline">Kestrel Dunmore Insurance Brokers</p>
  </div>
</section>

<section class="card card--back" aria-label="Card back">
  <div class="brand-block">
    <div class="brand">
      <span class="brand__square"></span>
      <span class="brand__name">kdib</span>
    </div>
    <p class="brand__tagline">Kestrel Dunmore Insurance Brokers</p>
  </div>

  <div class="contact">
    <h2 class="contact__name">KESTREL DUNMORE</h2>
    <p class="contact__row"><span class="contact__label">Phone:</span> 021 555 0148</p>
    <p class="contact__row"><span class="contact__label">Email:</span> kestrel@kdib.co.nz</p>
    <p class="contact__row"><span class="contact__label">Address:</span> P.O. Box 48 Waimea, NZ 70210</p>
  </div>

  <div class="footer-band"></div>
  <div class="web-tab">www.kdib.co.nz</div>
</section>

</body>
</html>
```